Garage Door Company seeking business card designs.
Harbor Ridge Door
Professional
Miles Tandry
Owner, Operator.
We don't want a address listed...
Miles@HarborRidgeDoor.com
www.PortalLiftExperts.com
We want to publish three numbers: Brinlow - 320.555.0147 Elmvale - 320.555.0192 Marrow - 952.555.0163 on front... Commercial and Residential On back... New Garage Door Sales and Installation. Repair and Maintenance Services. List website; www.PortalLiftExperts.com Have name, title, phone numbers, email, and website on one side. Motto's and verbiage on the other back side. Logo likely on front very prominently. Front can be full color, and back should be back letter, or the door of the logo lettering.
"If you can't get it up, we can!" Sales and Installation. Repair and Maintenance.

```html
<!DOCTYPE html>
<html lang="en">
<head>
<meta charset="utf-8">
<title>Harbor Ridge Door — Business Cards</title>
<link href="https://fonts.googleapis.com/css2?family=Open+Sans:wght@400;600;700&display=swap" rel="stylesheet">
<style>
  :root {
    --olive: #3c4a17;
    --olive-dark: #2f3a10;
    --olive-light: #6b7a45;
    --paper: #ffffff;
    --ink: #2b2b2b;
    --muted: #6a6a6a;
    --stage: #e9e9e6;
  }
  html, body {
    margin: 0;
    width: 1200px;
    height: 904px;
    overflow: hidden;
    background: var(--stage);
    font-family: "Open Sans", Arial, sans-serif;
  }
  .canvas {
    position: relative;
    width: 1200px;
    height: 904px;
  }
  .card {
    position: absolute;
    left: 250px;
    width: 700px;
    height: 400px;
    border-radius: 18px;
    overflow: hidden;
    box-shadow: 0 6px 18px rgba(0,0,0,0.18);
  }

  /* Back side */
  .card-back {
    top: 40px;
    background: var(--olive);
    color: var(--paper);
    text-align: center;
  }
  .back-mark {
    width: 190px;
    height: 110px;
    margin: 36px auto 0;
    border-radius: 6px;
    background: linear-gradient(180deg, #56663a, #3a4716);
    border: 1px solid rgba(255,255,255,0.35);
  }
  .back-name {
    margin: 12px 0 0;
    font-size: 30px;
    font-weight: 700;
    letter-spacing: 1px;
    text-transform: uppercase;
  }
  .back-motto {
    margin: 18px 0 0;
    font-size: 16px;
  }
  .back-services {
    margin: 16px 0 0;
    font-size: 16px;
    line-height: 1.35;
  }
  .back-web {
    margin: 26px auto 0;
    display: flex;
    align-items: center;
    justify-content: center;
    gap: 12px;
    font-size: 15px;
  }
  .back-web .rule {
    width: 40px;
    height: 1px;
    background: var(--paper);
  }

  /* Front side */
  .card-front {
    top: 464px;
    background: var(--paper);
    color: var(--ink);
  }
  .front-brand {
    position: absolute;
    left: 30px;
    top: 96px;
    width: 280px;
    text-align: center;
  }
  .front-mark {
    width: 220px;
    height: 120px;
    margin: 0 auto;
    border-radius: 6px;
    background: linear-gradient(180deg, #7d8b58, #3c4a17);
  }
  .front-name {
    margin: 12px 0 0;
    font-size: 24px;
    font-weight: 700;
    color: var(--olive);
    text-transform: uppercase;
    line-height: 1.1;
    white-space: nowrap;
  }
  .divider {
    position: absolute;
    left: 330px;
    top: 60px;
    width: 2px;
    height: 200px;
    background: var(--olive);
  }
  .contact {
    position: absolute;
    left: 356px;
    top: 62px;
  }
  .person-name {
    margin: 0;
    font-size: 22px;
    font-weight: 700;
    color: var(--ink);
  }
  .person-title {
    margin: 2px 0 16px;
    font-size: 14px;
    color: var(--muted);
  }
  .contact-list {
    list-style: none;
    margin: 0;
    padding: 0;
  }
  .contact-list li {
    display: flex;
    align-items: center;
    gap: 10px;
    font-size: 15px;
    line-height: 25px;
    color: var(--ink);
  }
  .icon {
    width: 16px;
    height: 16px;
    flex: none;
  }
  .service-band {
    position: absolute;
    right: 0;
    bottom: 34px;
    width: 380px;
    height: 44px;
  }
  .service-band span {
    position: absolute;
    right: 30px;
    top: 0;
    line-height: 44px;
    color: var(--paper);
    font-size: 16px;
    font-weight: 600;
  }
</style>
</head>
<body>
<main class="canvas">

  <section class="card card-back" aria-label="Back of business card">
    <div class="back-mark" role="img" aria-label="Company emblem illustration: garage house among pine trees"></div>
    <p class="back-name">Harbor Ridge Door</p>
    <p class="back-motto">“If you can't get it up, we can!”</p>
    <p class="back-services">Sales and Installation,<br>Repair and Maintenance</p>
    <div class="back-web"><span class="rule"></span>www.PortalLiftExperts.com<span class="rule"></span></div>
  </section>

  <section class="card card-front" aria-label="Front of business card">
    <div class="front-brand">
      <div class="front-mark" role="img" aria-label="Company emblem illustration: garage house among pine trees"></div>
      <p class="front-name">Harbor Ridge Door</p>
    </div>

    <div class="divider"></div>

    <div class="contact">
      <p class="person-name">Miles Tandry</p>
      <p class="person-title">Owner, Operator</p>
      <ul class="contact-list">
        <li><svg class="icon" viewBox="0 0 16 16"><circle cx="8" cy="8" r="8" fill="#3c4a17"/><path d="M5.2 4.2l1.3-.2.8 1.9-.9.7a5 5 0 0 0 2.9 2.9l.7-.9 1.9.8-.2 1.3c-3.9.2-6.7-2.6-6.5-6.5z" fill="#fff"/></svg>320.555.0147 (Brinlow)</li>
        <li><svg class="icon" viewBox="0 0 16 16"><circle cx="8" cy="8" r="8" fill="#3c4a17"/><path d="M5.2 4.2l1.3-.2.8 1.9-.9.7a5 5 0 0 0 2.9 2.9l.7-.9 1.9.8-.2 1.3c-3.9.2-6.7-2.6-6.5-6.5z" fill="#fff"/></svg>320.555.0192 (Elmvale)</li>
        <li><svg class="icon" viewBox="0 0 16 16"><circle cx="8" cy="8" r="8" fill="#3c4a17"/><path d="M5.2 4.2l1.3-.2.8 1.9-.9.7a5 5 0 0 0 2.9 2.9l.7-.9 1.9.8-.2 1.3c-3.9.2-6.7-2.6-6.5-6.5z" fill="#fff"/></svg>952.555.0163 (Marrow)</li>
        <li><svg class="icon" viewBox="0 0 16 16"><circle cx="8" cy="8" r="8" fill="#3c4a17"/><rect x="4" y="5" width="8" height="6" fill="none" stroke="#fff" stroke-width="1.1"/><path d="M4 5l4 3.3L12 5" fill="none" stroke="#fff" stroke-width="1.1"/></svg>Miles@HarborRidgeDoor.com</li>
        <li><svg class="icon" viewBox="0 0 16 16"><circle cx="8" cy="8" r="8" fill="#3c4a17"/><circle cx="8" cy="8" r="4" fill="none" stroke="#fff" stroke-width="1.1"/><path d="M4 8h8M8 4c-2 2.4-2 5.6 0 8M8 4c2 2.4 2 5.6 0 8" fill="none" stroke="#fff" stroke-width="0.9"/></svg>www.PortalLiftExperts.com</li>
      </ul>
    </div>

    <div class="service-band">
      <svg width="380" height="44" viewBox="0 0 380 44" aria-hidden="true"><path d="M24 0H380V44H0z" fill="#3c4a17"/></svg>
      <span>Commercial and Residential</span>
    </div>
  </section>

</main>
</body>
</html>
```